Dentist Ad for Airline Magazine

A full page print ad for magazine. Details below.

Target Market(s)

Mine workers and rural patients who fly in and out of the main city.

Industry/Entity Type

Airline

Requirements
Must have
• Copywriting as per attachment. Magazine print specifications as per attachment. Inviting colours (blue shades, perhaps some green/yellow). Comforting look and picture. Professional feel. Picture can be of a smiling or sleeping relaxed person (see business websites http://www.calmharbordentalcare.com and http://www.willowbankdentalclinic.com.au) - as we bring patients with complex dental problems or fear of the dentist, back to health whilst they enjoy a relaxing sleep (sedation).
Nice to have
• - stylised image of an aeroplane route across the text or at the footer

```html
<!DOCTYPE html>
<html lang="en">
<head>
<meta charset="utf-8">
<title>Fly-in and Fly-out Dental Transformations</title>
<link rel="stylesheet" href="https://fonts.googleapis.com/css2?family=Questrial&display=swap">
<style>
:root{
  --navy:#0f5f97;
  --band:#1771ad;
  --mid:#3d9bd6;
  --pale:#d9eef9;
  --chip:#5aa6d8;
  --panel:#84c6ee;
  --ink:#1c1c1c;
  --copy:#16679f;
  --sky:#a9dcf6;
  --white:#ffffff;
}
*{box-sizing:border-box;margin:0;padding:0}
html,body{width:927px;height:1200px;overflow:hidden;background:var(--white)}
body{font-family:"Questrial",sans-serif;color:var(--ink);position:relative}
.ad{position:absolute;left:20px;top:24px;width:888px;height:1157px}
.abs{position:absolute}
.header{left:0;top:0;width:888px;height:96px;background:var(--navy);color:var(--white);
  font-size:27px;line-height:33px;text-align:center;padding-top:14px}
.intro{left:0;top:96px;width:888px;height:251px;
  background:radial-gradient(ellipse at 30% 30%,#f3fafe 0%,var(--pale) 60%,#c8e5f5 100%)}
.chip{background:var(--chip);color:var(--ink);font-size:17px;line-height:21px;border-radius:3px;
  padding:5px 8px;text-align:right}
.chip.wide{text-align:left}
.intro-copy{left:30px;top:167px;width:828px;font-size:20px;line-height:24.5px;color:var(--copy);text-align:center}
.why{left:0;top:347px;width:888px;height:323px;background:var(--mid)}
.photo{border:4px solid var(--white);background:linear-gradient(160deg,#cfe6f2,#7fb4cf 60%,#4f8a6a)}
.why-tab{left:131px;top:9px;width:757px;height:34px;background:var(--band);border-radius:17px 0 0 17px;
  color:var(--white);font-size:21px;line-height:34px;padding-left:24px}
.why-list{left:176px;top:54px;width:695px;list-style:none;font-size:17px;line-height:21px;color:var(--ink)}
.why-list li{margin-bottom:21px}
.promise{left:0;top:670px;width:888px;height:178px;background:var(--band);text-align:center;font-size:21px;line-height:26px}
.promise .lead{color:var(--white);padding-top:23px}
.promise .reach{color:var(--sky);margin-top:26px}
.footer{left:0;top:848px;width:888px;height:309px;background:var(--mid)}
.contact-panel{left:73px;top:20px;width:795px;height:259px;background:var(--panel);border-radius:14px}
.call{left:30px;top:12px;font-size:23px;color:var(--ink);letter-spacing:.3px}
.rule{left:30px;top:44px;width:418px;height:2px;background:var(--white)}
.brand{display:flex;align-items:center;gap:10px;font-size:28px;color:#1f3f66}
.brand .dot{width:30px;height:30px;border-radius:50%;background:var(--navy)}
.brand.alt{font-size:20px;color:#4b4b4b}
.brand.alt .dot{width:34px;height:34px;background:#4aa9dd}
.card{width:330px;text-align:center;font-size:17px;line-height:23px;color:var(--ink)}
.address{left:0;top:220px;width:795px;text-align:center;font-size:17px;color:var(--ink)}
</style>
</head>
<body>
<main class="ad">
  <header class="abs header">
    <h1 style="font-weight:400;font-size:27px">Fly-in and Fly-out Dental Transformations<br>True Care, Advanced Expertise, Minimal Visits</h1>
  </header>

  <section class="abs intro">
    <div class="abs chip" style="left:240px;top:20px;width:218px">Embarassed to Smile?</div>
    <div class="abs chip" style="left:190px;top:58px;width:268px">Complex dental problems?</div>
    <div class="abs chip" style="left:124px;top:98px;width:334px">No time for endless appointments?</div>
    <div class="abs chip wide" style="left:450px;top:20px;width:347px">Do you suffer from fear of the dentist or just can’t find the right one?</div>
    <div class="abs chip wide" style="left:450px;top:76px;width:347px">Do you wish you could just sleep your way to a healthy and attractive smile?</div>
    <p class="abs intro-copy">If the answer is yes to any of these questions, you are certainly not alone! In our specialized Sleep Dentistry Centre, our renowned team provides gentle, compassionate, advanced and extensive treatments often in the comfort of a relaxing sleep (IV Sedation).</p>
  </section>

  <section class="abs why">
    <div class="abs photo" style="left:9px;top:9px;width:114px;height:145px" role="img" aria-label="Photo of a happy couple smiling outdoors"></div>
    <div class="abs photo" style="left:9px;top:163px;width:114px;height:150px" role="img" aria-label="Portrait photo of a smiling young man"></div>
    <h2 class="abs why-tab" style="font-weight:400">WHY US?</h2>
    <ul class="abs why-list">
      <li>- We take the time to understand your needs so you can make the best decisions for your health. You are looked after by a friendly, highly qualified expert team in relaxed and comfortable surroundings.</li>
      <li>- Our patients often have treatments that would normally take months completed in minimal visits – which is perfect for the Fly-in, Fly-out patient.</li>
      <li>- We offer a full range of dental treatments including dental implant surgeries and cosmetic rehabilitations all in-house.</li>
      <li>- Our approach with Sleep Dentistry means Pain-Free, anxiety free, memory free procedures. Just excellent results and life changing treatments.</li>
    </ul>
  </section>

  <section class="abs promise">
    <p class="lead">SOUND TOO GOOD TO BE TRUE? IT’S JUST WHAT WE DO FOR<br>OUR PATIENTS EVERY DAY.</p>
    <p class="reach">OUR PATIENTS COME FROM ALL OVER WESTERN AUSTRALIA TO TAKE<br>ADVANTAGE OF THIS UNIQUE AND PERSONALIZED SERVICE. WE INVITE YOU</p>
  </section>

  <footer class="abs footer">
    <div class="abs contact-panel">
      <p class="abs call">CALL OUR FRIENDLY TEAM TODAY</p>
      <div class="abs rule"></div>
      <div class="abs brand" style="left:42px;top:70px"><span class="dot"></span>Willowbank Dental</div>
      <div class="abs brand alt" style="left:470px;top:20px;width:260px"><span class="dot"></span>Calm Harbor Dental Care</div>
      <div class="abs card" style="left:78px;top:118px">
        Willowbank Dental Clinic<br>9470 5512<br>www.willowbankdentalclinic.com.au<br>info@willowbankdentalclinic.com.au
      </div>
      <div class="abs card" style="left:400px;top:118px">
        Calm Harbor Dental Care<br>9470 5510<br>www.calmharbordentalcare.com<br>info@calmharbordentalcare.com
      </div>
      <p class="abs address">48 Harbour Lane Westmere WA 6017</p>
    </div>
  </footer>
</main>
</body>
</html>
```